Regional Consulting Business Needs a Business Card Design

We need a business card design for our new business based in Regional Victoria, Australia called Brindle Power. We are a consulting company with our main goal being to save people momey money and reducing their carbon footprint. Anything from water saving showerheads, to energy saving lightglobes and even to solar power. We would like to see designs that use bright colours. The final design should shout 'we are here to help you'.

Industry/Entity Type

Business

```html
<!DOCTYPE html>
<html lang="en">
<head>
<meta charset="utf-8">
<title>Brindle Power – Business Card</title>
<link rel="stylesheet" href="https://fonts.googleapis.com/css2?family=Open+Sans:ital,wght@0,400;0,600;0,700;1,400&display=swap">
<style>
  :root {
    --backdrop: #1f1f21;
    --card: #ffffff;
    --card-shade: #e9e9ea;
    --ink: #2b2b2b;
    --ink-soft: #4a4a4a;
    --logo-grey: #6b6b6b;
    --accent: #f3a31b;
    --accent-deep: #e08a0b;
    --band-dark: #1c1c1c;
  }
  * { margin: 0; padding: 0; box-sizing: border-box; }
  html, body { width: 1200px; height: 944px; overflow: hidden; }
  body {
    background: var(--backdrop);
    font-family: "Open Sans", Arial, sans-serif;
    position: relative;
  }
  .card {
    position: absolute;
    background: linear-gradient(180deg, var(--card) 55%, var(--card-shade) 100%);
    border-radius: 26px;
    overflow: hidden;
    box-shadow: 0 10px 30px rgba(0,0,0,.5);
  }
  .card-front { left: 70px; top: 110px; width: 580px; height: 340px; }
  .card-back  { left: 550px; top: 480px; width: 590px; height: 350px; }

  .brand { display: flex; align-items: center; gap: 12px; }
  .brand-mark { width: 34px; height: 34px; background: var(--accent); }
  .brand-name { font-weight: 700; color: var(--logo-grey); }
  .brand-tagline { font-weight: 700; color: var(--ink); }

  .card-front .brand { position: absolute; left: 120px; top: 100px; }
  .card-front .brand-name { font-size: 44px; line-height: 1; }
  .card-front .brand-tagline { position: absolute; left: 166px; top: 158px; font-size: 17px; }
  .card-front .website {
    position: absolute; left: 0; right: 0; top: 260px;
    text-align: center; font-size: 18px; letter-spacing: 1px; color: var(--ink);
  }

  .card-back .brand { position: absolute; left: 238px; top: 40px; gap: 10px; }
  .card-back .brand-mark { width: 26px; height: 26px; }
  .card-back .brand-name { font-size: 33px; line-height: 1; }
  .card-back .brand-tagline { position: absolute; left: 262px; top: 84px; font-size: 13px; }

  .person { position: absolute; left: 56px; top: 112px; }
  .person-name { font-size: 24px; color: var(--ink); line-height: 1.1; }
  .person-role { font-size: 14px; font-style: italic; color: var(--accent); }

  .address { position: absolute; left: 40px; top: 174px; display: flex; gap: 8px; }
  .address p { font-size: 16px; line-height: 1.3; color: var(--ink-soft); }

  .contacts { position: absolute; left: 338px; top: 178px; list-style: none; }
  .contacts li {
    display: flex; align-items: center; gap: 8px;
    font-size: 16px; line-height: 1.3; color: var(--ink-soft);
  }
  .icon { width: 14px; height: 14px; flex: none; }
  .swoosh { position: absolute; left: 0; bottom: 0; width: 100%; height: 110px; }
</style>
</head>
<body>

  <section class="card card-front" aria-label="Card front">
    <div class="brand">
      <span class="brand-mark"></span>
      <span class="brand-name">Brindle Power</span>
    </div>
    <p class="brand-tagline">Maintanence and consulting services</p>
    <p class="website">www.brindlepower.com</p>
  </section>

  <section class="card card-back" aria-label="Card back">
    <div class="brand">
      <span class="brand-mark"></span>
      <span class="brand-name">Brindle Power</span>
    </div>
    <p class="brand-tagline">Maintanence and consulting services</p>

    <div class="person">
      <p class="person-name">Martin Kessler</p>
      <p class="person-role">director</p>
    </div>

    <div class="address">
      <svg class="icon" viewBox="0 0 14 14" aria-hidden="true">
        <path d="M7 1 L13 7 H11 V13 H3 V7 H1 Z" fill="var(--accent)"/>
      </svg>
      <p>48 Ferris Lane<br>Suite 12-140<br>Ballarat, VIC 3350</p>
    </div>

    <ul class="contacts">
      <li>
        <svg class="icon" viewBox="0 0 14 14" aria-hidden="true"><circle cx="7" cy="7" r="6" fill="none" stroke="var(--accent)" stroke-width="2"/><path d="M5 4 Q4 8 8 10" stroke="var(--accent)" stroke-width="2" fill="none"/></svg>
        555-013-2200
      </li>
      <li>
        <svg class="icon" viewBox="0 0 14 14" aria-hidden="true"><rect x="1" y="6" width="12" height="7" rx="1" fill="var(--accent)"/><rect x="3" y="1" width="8" height="5" fill="none" stroke="var(--accent)" stroke-width="1.5"/></svg>
        555-013-2201
      </li>
      <li>
        <svg class="icon" viewBox="0 0 14 14" aria-hidden="true"><rect x="1" y="3" width="12" height="9" rx="1" fill="var(--accent)"/><path d="M1 3 L7 8 L13 3" stroke="#fff" stroke-width="1.2" fill="none"/></svg>
        info@brindlepower.com
      </li>
      <li>
        <svg class="icon" viewBox="0 0 14 14" aria-hidden="true"><circle cx="7" cy="7" r="6.5" fill="var(--accent)"/></svg>
        www.brindlepower.com
      </li>
    </ul>

    <svg class="swoosh" viewBox="0 0 590 110" preserveAspectRatio="none" aria-hidden="true">
      <defs>
        <linearGradient id="accentGrad" x1="0" y1="0" x2="0" y2="1">
          <stop offset="0" stop-color="var(--accent)"/>
          <stop offset="1" stop-color="var(--accent-deep)"/>
        </linearGradient>
      </defs>
      <path d="M0 40 C150 20 300 70 590 30 L590 110 L0 110 Z" fill="var(--band-dark)"/>
      <path d="M0 58 C160 40 320 85 590 48 L590 110 L0 110 Z" fill="url(#accentGrad)"/>
      <path d="M0 78 C180 62 340 100 590 72 L590 110 L0 110 Z" fill="#ffffff" opacity=".25"/>
    </svg>
  </section>

</body>
</html>
```